Rise As Captain Book Cover Design

Book Cover Design Brief
Book Title
Rise As Captain
Subtitle
The 10 Quiet Habits of Remarkable Command
Author
Orwen Dalquist
Overview
This book is about leadership that starts within.
Most leadership books focus on tactics or management strategies. This book focuses on the inner disciplines that create powerful leaders — mindset, integrity, focus, empathy, professionalism, honesty, and self-respect.
The tone of the book is bold, direct, confident, and transformational.
This is not a soft or corporate leadership book. It is a call to step up and become the leader you are capable of becoming.
The cover should feel:
• Powerful
• Professional
• Transformational
• Premium
• Memorable
Think best-selling leadership book, not a generic business book.
Target Audience
Business owners
Managers
Entrepreneurs
Team leaders
Professionals who want to grow as leaders
Most readers are ambitious professionals who want to level up their leadership and life.
Design Direction
The design should communicate:
Strength. Discipline. Leadership. Personal transformation.
Avoid cliché leadership visuals like:
• Handshakes
• Office buildings
• Corporate stock imagery
• Teams sitting around tables
The design should feel iconic, bold, and timeless.
Think about covers of successful leadership books such as:
Copper Rituals
Total Stewardship
Won't Break Now
Begin From Purpose
The 36 Rules of Sway
These covers are simple, powerful, and recognizable even at small sizes.
Typography
The title RISE AS CAPTAIN should be:
• Bold
• Strong
• Dominant on the cover
• Easy to read even at small sizes (important for Vellora thumbnails)
The subtitle should be clean and secondary to the title.
The overall typography should feel strong, modern, and premium.
Color Direction
Designers are free to explore colors, but the cover should feel strong and premium, not playful.
Colors that often work well for leadership books include:
Black
Gold
White
Deep blue
Dark red
High contrast and clarity are important.
Style
Preferred style:
• Clean
• Modern
• Minimal
• Strong contrast
Avoid clutter and overly busy designs.
The goal is to create a cover that feels powerful and professional at first glance.
Deliverables
Front cover design for a leadership book.
Final files should include:
• High resolution artwork
• Editable source files
• Print-ready version suitable for publishing
Goal of the Cover
When someone sees this book on Vellora or in a bookstore, they should immediately think:
“This looks like a serious leadership book.”
The design should feel like it belongs next to books by authors such as:
Marcus Thorley
Brandt Osgood
Peter Hollis
Nolan Fairbrook
A strong, confident cover that attracts leaders who want to grow and perform at a higher level.
Target Market(s)
Business Owners and High level managers
Look and feel
Each slider illustrates characteristics of the customer's brand and the style your logo design should communicate.

```html
<!DOCTYPE html>
<html lang="en">
<head>
<meta charset="utf-8">
<title>Rise As Captain — Book Cover</title>
<link href="https://fonts.googleapis.com/css2?family=Archivo:wght@600;700;900&display=swap" rel="stylesheet">
<style>
  :root {
    --backdrop: #3a3a3a;
    --paper: #e7e5e0;
    --paper-shade: #d8d5ce;
    --title-gold: #93591a;
    --subtitle-brown: #35201a;
    --author-white: #f4efe8;
    --haze-light: rgba(238, 222, 196, 0.9);
    --haze-amber: #b5793c;
    --earth-mid: #6b4424;
    --earth-deep: #3b2414;
    --earth-dark: #1a110a;
  }
  * { box-sizing: border-box; margin: 0; padding: 0; }
  html, body {
    width: 1200px;
    height: 800px;
    overflow: hidden;
    background: var(--backdrop);
  }
  .canvas {
    position: relative;
    width: 1200px;
    height: 800px;
    background: var(--backdrop);
  }
  .book-cover {
    position: absolute;
    left: 348px;
    top: 40px;
    width: 504px;
    height: 720px;
    overflow: hidden;
    background: radial-gradient(ellipse at 50% 30%, var(--paper) 0%, var(--paper-shade) 100%);
    font-family: "Archivo", "Arial", sans-serif;
    text-align: center;
  }
  .cover-scene {
    position: absolute;
    left: 0;
    right: 0;
    top: 230px;
    bottom: 0;
    background:
      radial-gradient(ellipse 16% 62% at 50% 62%, rgba(196, 128, 70, 0.55) 0%, rgba(196, 128, 70, 0) 100%),
      radial-gradient(ellipse 30% 22% at 50% 36%, var(--haze-light) 0%, rgba(238, 222, 196, 0) 100%),
      radial-gradient(ellipse 38% 60% at 0% 100%, rgba(26, 17, 10, 0.85) 0%, rgba(26, 17, 10, 0) 100%),
      radial-gradient(ellipse 38% 60% at 100% 100%, rgba(20, 13, 8, 0.9) 0%, rgba(20, 13, 8, 0) 100%),
      linear-gradient(to bottom,
        rgba(231, 229, 224, 0) 0%,
        rgba(226, 206, 176, 0.6) 18%,
        rgba(201, 150, 96, 0.85) 34%,
        var(--haze-amber) 46%,
        var(--earth-mid) 62%,
        var(--earth-deep) 80%,
        var(--earth-dark) 100%);
  }
  .title {
    position: absolute;
    left: 0;
    right: 0;
    top: 80px;
    color: var(--title-gold);
    font-weight: 900;
    line-height: 0.86;
    letter-spacing: -1px;
    text-transform: uppercase;
  }
  .title-lead {
    display: block;
    font-size: 52px;
  }
  .title-main {
    display: block;
    font-size: 80px;
    margin-top: 4px;
  }
  .subtitle {
    position: absolute;
    left: 0;
    right: 0;
    top: 200px;
    color: var(--subtitle-brown);
    font-weight: 700;
    font-size: 17px;
    line-height: 1.08;
    text-transform: uppercase;
  }
  .author {
    position: absolute;
    left: 0;
    right: 0;
    top: 672px;
    color: var(--author-white);
    font-weight: 700;
    font-size: 18px;
    letter-spacing: 0.4px;
    text-transform: uppercase;
  }
</style>
</head>
<body>
  <main class="canvas">
    <article class="book-cover">
      <div class="cover-scene" role="img" aria-label="Silhouette of a man standing at the top of a long staircase rising above a hazy city skyline at sunrise, in warm amber and brown tones"></div>
      <h1 class="title">
        <span class="title-lead">Rise As</span>
        <span class="title-main">Captain</span>
      </h1>
      <p class="subtitle">The 10 Quiet Habits<br>of Remarkable Command</p>
      <p class="author">Orwen Dalquist</p>
    </article>
  </main>
</body>
</html>
```